Dune Air & Plus business card

I need an awesome, double-sided business card designed with our new logo. I would like the one side black with the colored logo, and the back side is all yours. I'd like to see horizontal and vertical layouts. Get creative! Thank you.

Target Market(s)

HVAC, Heating and Cooling in Phoenix, AZ

Industry/Entity Type

HVAC

Contact Information for Business Card

We need our new logo on the card. Tom Harker, (623) 555-0142, tom@trydunesair.com, www.trydunesair.com, ROC 514273

```html
<!DOCTYPE html>
<html lang="en">
<head>
<meta charset="utf-8">
<title>Dune Air &amp; Plus – Business Card</title>
<link rel="stylesheet" href="https://fonts.googleapis.com/css2?family=Montserrat:wght@400;500;800&display=swap">
<style>
  :root {
    --canvas: #ecebe8;
    --card-dark: #1e1e1e;
    --card-light: #ffffff;
    --brand-blue: #1b7fd6;
    --brand-orange: #f26b21;
    --ink: #2b2b2b;
  }
  * { box-sizing: border-box; margin: 0; padding: 0; }
  html, body {
    width: 1200px;
    height: 900px;
    overflow: hidden;
    background: var(--canvas);
    font-family: "Montserrat", sans-serif;
  }
  .stage {
    position: relative;
    width: 1200px;
    height: 900px;
  }
  .card {
    position: absolute;
    left: 280px;
    width: 640px;
    height: 366px;
    border-radius: 22px;
    box-shadow: 0 10px 28px rgba(0,0,0,0.18);
  }
  .card--front {
    top: 66px;
    background: var(--card-dark);
    display: flex;
    align-items: center;
    justify-content: center;
  }
  .card--back {
    top: 468px;
    background: var(--card-light);
  }
  .wordmark {
    display: flex;
    align-items: center;
    gap: 14px;
  }
  .wordmark__dot {
    width: 30px;
    height: 30px;
    border-radius: 50%;
    background: var(--brand-orange);
    flex: none;
  }
  .wordmark__name {
    font-weight: 800;
    color: var(--brand-blue);
    text-transform: uppercase;
    letter-spacing: 0.5px;
    line-height: 1;
  }
  .card--front .wordmark__name { font-size: 40px; }
  .card--back .wordmark {
    position: absolute;
    left: 44px;
    top: 162px;
    gap: 10px;
  }
  .card--back .wordmark__dot { width: 22px; height: 22px; }
  .card--back .wordmark__name { font-size: 26px; }
  .divider {
    position: absolute;
    left: 340px;
    top: 86px;
    width: 2px;
    height: 198px;
    background: var(--brand-blue);
  }
  .contact {
    position: absolute;
    left: 372px;
    top: 74px;
    color: var(--ink);
  }
  .contact__name {
    font-weight: 800;
    font-size: 27px;
    letter-spacing: 0.5px;
    text-transform: uppercase;
    line-height: 1;
  }
  .contact__first { color: var(--brand-blue); }
  .contact__last { color: var(--brand-orange); }
  .contact__role {
    font-size: 14px;
    font-weight: 500;
    margin-top: 6px;
  }
  .contact__address {
    font-size: 14px;
    line-height: 1.45;
    margin-top: 18px;
  }
  .contact__list {
    list-style: none;
    margin-top: 14px;
    font-size: 14px;
    line-height: 1.5;
  }
  .contact__list li {
    display: flex;
    align-items: center;
    gap: 8px;
  }
  .contact__list svg {
    width: 12px;
    height: 12px;
    flex: none;
    fill: none;
    stroke: var(--brand-orange);
    stroke-width: 1.6;
  }
  .contact__license { padding-left: 20px; }
</style>
</head>
<body>
<main class="stage">

  <section class="card card--front" aria-label="Card front">
    <div class="wordmark">
      <span class="wordmark__dot"></span>
      <span class="wordmark__name">Dune Air &amp; Plus</span>
    </div>
  </section>

  <section class="card card--back" aria-label="Card back">
    <div class="wordmark">
      <span class="wordmark__dot"></span>
      <span class="wordmark__name">Dune Air &amp; Plus</span>
    </div>

    <div class="divider"></div>

    <div class="contact">
      <h1 class="contact__name"><span class="contact__first">Tom</span> <span class="contact__last">Harker</span></h1>
      <p class="contact__role">Director</p>
      <p class="contact__address">1460 Saguaro Lane<br>Tempe, AZ 85281</p>
      <ul class="contact__list">
        <li>
          <svg viewBox="0 0 12 12"><path d="M2.5 1.2 L4.3 1.2 L5 3.6 L3.8 4.6 C4.5 6 5.9 7.4 7.4 8.2 L8.4 7 L10.8 7.7 L10.8 9.5 C10.8 10.3 10.2 10.9 9.4 10.8 C5.2 10.4 1.6 6.8 1.2 2.6 C1.1 1.8 1.7 1.2 2.5 1.2 Z"/></svg>
          (623) 555-0142
        </li>
        <li>
          <svg viewBox="0 0 12 12"><rect x="1" y="2.5" width="10" height="7" rx="0.8"/><path d="M1.3 3 L6 6.6 L10.7 3"/></svg>
          tom@trydunesair.com
        </li>
        <li>
          <svg viewBox="0 0 12 12"><circle cx="6" cy="6" r="4.8"/><ellipse cx="6" cy="6" rx="2" ry="4.8"/><path d="M1.2 6 H10.8"/></svg>
          www.trydunesair.com
        </li>
        <li class="contact__license">ROC 514273</li>
      </ul>
    </div>
  </section>

</main>
</body>
</html>
```